Manufacturers Catalog Cover Page

We are looking to have a cover to our catalog page designed. I currently have begun work for the remained of the catalog in InDesign and want the cover created in InDesign. I will provide photos.

Looking to beable to add the cover to our existing attached catalog.

Industry/Entity Type

Manufacturing

Requirements
Must have
• Colors match what we are currently using. The Dark grey and gold
Nice to have
• modern, clean

```html
<!DOCTYPE html>
<html lang="en">
<head>
<meta charset="utf-8">
<title>Catalog Cover – Meridian Polymers</title>
<link href="https://fonts.googleapis.com/css2?family=Bebas+Neue&family=Montserrat:wght@400;700&display=swap" rel="stylesheet">
<style>
  :root{
    --bg:#c9c9c9;
    --charcoal:#414042;
    --charcoal-dark:#39383a;
    --gold:#d7b97a;
    --gold-deep:#b9a055;
    --white:#ffffff;
  }
  html,body{margin:0;padding:0;width:1200px;height:1200px;overflow:hidden;background:var(--bg);}
  .canvas{position:relative;width:1200px;height:1200px;}
  .spread{
    position:absolute;left:0;top:175px;width:1341px;height:949px;
    transform:scale(0.8948);transform-origin:0 0;
    background:var(--charcoal);overflow:hidden;
  }
  .block{position:absolute;}
  .white{background:var(--white);}
  .gold{background:var(--gold);}
  .gold-deep{background:var(--gold-deep);}
  .dark{background:var(--charcoal);}
  .spine{position:absolute;left:670px;top:0;width:1px;height:949px;background:var(--charcoal-dark);}

  .title{position:absolute;left:730px;top:94px;font-family:"Bebas Neue",sans-serif;color:var(--white);}
  .title .sub{font-size:34px;line-height:32px;letter-spacing:.2px;}
  .title .main{margin-top:6px;font-size:68px;line-height:62px;color:var(--gold);}

  .brand{position:absolute;left:1107px;top:104px;display:flex;align-items:center;gap:12px;}
  .brand-dot{width:58px;height:58px;border:4px solid var(--gold);border-radius:50%;box-sizing:border-box;}
  .brand-name{font-family:"Bebas Neue",sans-serif;font-size:28px;line-height:31px;color:var(--white);text-align:center;}

  .contact{position:absolute;left:78px;top:452px;font-family:"Montserrat",sans-serif;color:#3b3a3c;font-size:13.5px;line-height:16px;}
  .contact h3{margin:0 0 10px;font-size:13.5px;font-weight:700;}
  .contact .row{display:flex;gap:6px;margin-bottom:10px;width:220px;}
  .contact svg{flex:none;width:18px;height:18px;}

  .about{position:absolute;left:78px;top:720px;width:552px;font-family:"Montserrat",sans-serif;}
  .about h2{margin:0 0 6px;font-size:20px;font-weight:700;color:var(--gold);}
  .about p{margin:0;font-size:13.4px;line-height:18px;color:var(--white);text-align:justify;}

  .reach{position:absolute;right:284px;top:842px;text-align:right;font-family:"Bebas Neue",sans-serif;color:var(--white);}
  .reach .phones{font-size:29px;line-height:30px;}
  .reach .web{font-size:29px;line-height:30px;}
  .reach .web span{color:var(--gold);}

  .photo{position:absolute;}
</style>
</head>
<body>
<div class="canvas">
  <div class="spread">
    <!-- white gutters -->
    <div class="block white" style="left:0;top:372px;width:1341px;height:283px;"></div>
    <div class="block white" style="left:937px;top:0;width:404px;height:372px;"></div>
    <div class="block white" style="left:1081px;top:372px;width:260px;height:577px;"></div>
    <div class="block white" style="left:809px;top:649px;width:278px;height:178px;"></div>

    <div class="spine"></div>

    <!-- left page -->
    <div class="block gold" style="left:0;top:378px;width:307px;height:271px;"></div>
    <div class="photo" role="img" aria-label="Modern glass office building with landscaping" style="left:313px;top:378px;width:175px;height:271px;background:linear-gradient(180deg,#9fbfe0 0%,#c9ccca 40%,#7e8d96 75%,#6f8a55 100%);"></div>
    <div class="photo" role="img" aria-label="Yellow combine harvester in a wheat field under a cloudy sky" style="left:493px;top:378px;width:177px;height:177px;background:linear-gradient(180deg,#8fb6dc 0%,#dfe6ec 40%,#d8b64a 65%,#c9a56a 100%);"></div>
    <div class="block gold" style="left:493px;top:559px;width:177px;height:90px;"></div>

    <div class="contact">
      <h3>CONTACT US</h3>
      <div class="row">
        <svg viewBox="0 0 18 18"><circle cx="9" cy="9" r="8" fill="none" stroke="#3b3a3c" stroke-width="1.3"/><path d="M4.5 9.5 9 5l4.5 4.5M6 8.5V13h6V8.5" fill="none" stroke="#3b3a3c" stroke-width="1.3"/></svg>
        <span>ptatautquidemfuga.ltae.lme molum qui is ut eum essus quat doluptatiori.</span>
      </div>
      <div class="row">
        <svg viewBox="0 0 18 18"><circle cx="9" cy="9" r="8" fill="none" stroke="#3b3a3c" stroke-width="1.3"/><path d="M6 5c-1 1-1 2.5.5 4.5s3 3 4.5 3.5c1 .3 1.8-.2 2.2-.8l-1.7-1.5-1.2.8c-1-.5-2.2-1.7-2.7-2.7l.8-1.2L7 5z" fill="#3b3a3c"/></svg>
        <span>987654321</span>
      </div>
      <div class="row">
        <svg viewBox="0 0 18 18"><circle cx="9" cy="9" r="8" fill="none" stroke="#3b3a3c" stroke-width="1.3"/><rect x="4.5" y="6" width="9" height="6.5" fill="none" stroke="#3b3a3c" stroke-width="1.2"/><path d="M4.5 6 9 9.5 13.5 6" fill="none" stroke="#3b3a3c" stroke-width="1.2"/></svg>
        <span>mail@domain.com</span>
      </div>
      <div class="row">
        <svg viewBox="0 0 18 18"><circle cx="9" cy="9" r="8" fill="none" stroke="#3b3a3c" stroke-width="1.3"/><circle cx="9" cy="9" r="4" fill="none" stroke="#3b3a3c" stroke-width="1.2"/><path d="M5 9h8M9 5v8" stroke="#3b3a3c" stroke-width="1"/></svg>
        <span>www.samplestudio.com</span>
      </div>
    </div>

    <div class="about">
      <h2>DECUM MOLTUS EGO VAT, NOCA; HACERDIT.</h2>
      <p>Moeris iam adductur publium vivitam quonferobse nirmis hos audemusquam ego ese abescerfex niquium hoctod prae tatu quamditam seniquid Cupion Etratis. Potast L. Cupecum ocultur publintia? Opiempo ridiessate nondiem mortuus, quossatiam enducto rtissa confece raris; notius pre, nortertintra ditiam oc, que nox morius, nosu mordi, C. Vivid compert ierisse nterena, mo</p>
    </div>

    <!-- right page -->
    <div class="title">
      <div class="sub">RUBBER &amp; PLASTIC<br>EXTURSION</div>
      <div class="main">GASKETS<br>TRIMS &amp;<br>SEALS</div>
    </div>

    <div class="block gold" style="left:943px;top:0;width:138px;height:205px;"></div>
    <div class="block dark" style="left:1087px;top:0;width:254px;height:205px;"></div>
    <div class="brand">
      <div class="brand-dot"></div>
      <div class="brand-name">MERIDIAN<br>POLYMERS</div>
    </div>

    <div class="photo" role="img" aria-label="Black rubber edge trim profiles" style="left:943px;top:211px;width:138px;height:161px;background:linear-gradient(135deg,#f3eef2 0%,#d8d3d8 45%,#3a3a3c 70%,#efeaee 100%);"></div>
    <div class="photo" role="img" aria-label="Yellow industrial robots on a factory line" style="left:1087px;top:211px;width:254px;height:161px;background:linear-gradient(135deg,#8fb5d6 0%,#e2c12a 40%,#6e7f93 70%,#cfd8df 100%);"></div>
    <div class="photo" role="img" aria-label="Oil refinery towers reflected in water at dusk" style="left:671px;top:378px;width:410px;height:177px;background:linear-gradient(180deg,#5f8fb8 0%,#b5c8d4 40%,#8a6a52 55%,#6e7c86 75%,#a9a9a4 100%);"></div>
    <div class="photo" role="img" aria-label="White motor yacht speeding across blue water" style="left:1087px;top:378px;width:254px;height:136px;background:linear-gradient(160deg,#2f6f9f 0%,#5a94bb 40%,#dfe4e8 60%,#1f5a86 100%);"></div>
    <div class="photo" role="img" aria-label="Rolls of rubber seal strips with adhesive backing" style="left:1087px;top:519px;width:254px;height:132px;background:linear-gradient(135deg,#f6f3f0 0%,#2b2b2d 35%,#d9bf9a 55%,#d24a2c 80%,#f4f1ee 100%);"></div>
    <div class="block gold-deep" style="left:671px;top:561px;width:138px;height:88px;"></div>
    <div class="photo" role="img" aria-label="Assorted rubber and silicone tubing profiles" style="left:815px;top:561px;width:266px;height:88px;background:linear-gradient(90deg,#f3eeea 0%,#8a4f3a 35%,#ebe6df 60%,#d8562e 85%,#f3eeea 100%);"></div>
    <div class="block gold-deep" style="left:1087px;top:655px;width:254px;height:42px;"></div>
    <div class="photo" role="img" aria-label="Motorhome coach on a desert highway" style="left:815px;top:655px;width:266px;height:166px;background:linear-gradient(180deg,#c08a62 0%,#6b5a48 40%,#5c5244 70%,#9a9a96 100%);"></div>
    <div class="block gold" style="left:1087px;top:703px;width:47px;height:246px;"></div>
    <div class="photo" role="img" aria-label="Orange backhoe excavator digging under a blue sky" style="left:1140px;top:703px;width:201px;height:246px;background:linear-gradient(180deg,#3f86c8 0%,#9ec3e2 45%,#d6902e 70%,#8a5a36 100%);"></div>

    <div class="reach">
      <div class="phones">555-014-2290 &nbsp;|&nbsp; 555-013-7741</div>
      <div class="web">WWW.<span>MERIDIANPOLYMERS</span>.COM</div>
    </div>
  </div>
</div>
</body>
</html>
```